Design some Business Cards @ Letter Heads for Quorvastem

Logo is available to download at

https://www.filevaultly.net/sh/ke82pq04x1zz9m/TRw7Lb2Qx8
Corporate design needed. I need to be able to import letterhead template into word without any problems.

Business cards I want to be able to edit names and contact details if possible for future employees in adobe or something.

Two side business cards please.

```html
<!DOCTYPE html>
<html lang="en">
<head>
<meta charset="utf-8">
<title>Quorvastem – Business Card, Front and Back</title>
<link href="https://fonts.googleapis.com/css2?family=Open+Sans:wght@400;600&display=swap" rel="stylesheet">
<style>
  :root{
    --stage:#e4e6ec;
    --brand-blue:#27a9dc;
    --brand-blue-light:#45c4ec;
    --brand-blue-deep:#1690c4;
    --panel-grey:#7c7f82;
    --panel-grey-dark:#67696c;
    --ink:#3e4245;
    --paper:#f7f8f8;
    --white:#ffffff;
  }
  *{box-sizing:border-box;margin:0;padding:0}
  html,body{width:1200px;height:820px;overflow:hidden}
  body{
    background:var(--stage);
    font-family:"Open Sans",Arial,sans-serif;
    position:relative;
  }
  .card{
    position:absolute;
    width:600px;height:343px;
    border-radius:3px;
    overflow:hidden;
    box-shadow:0 10px 24px rgba(40,50,70,.18);
  }

  /* Side A */
  .card-front{
    left:150px;top:58px;
    background:radial-gradient(ellipse at 50% 45%,var(--brand-blue-light) 0%,var(--brand-blue) 55%,var(--brand-blue-deep) 100%);
    color:var(--white);
    text-align:center;
  }
  .card-front .wordmark{
    position:absolute;left:0;right:0;top:118px;
    font-size:52px;font-weight:600;letter-spacing:-.5px;
  }
  .card-front .website{
    position:absolute;left:0;right:0;top:232px;
    font-size:13px;letter-spacing:1px;
  }

  /* Side B */
  .card-back{left:450px;top:420px;background:var(--paper)}
  .card-back svg.artwork{position:absolute;inset:0}
  .card-back .wordmark{
    position:absolute;left:34px;top:96px;
    font-size:44px;font-weight:600;letter-spacing:-.5px;
    color:var(--brand-blue);
  }
  .holder{position:absolute;left:38px;top:184px}
  .holder-name{font-size:30px;color:var(--ink);line-height:1.1}
  .holder-role{font-size:17px;color:var(--brand-blue);font-weight:600}
  .contact-list{
    position:absolute;right:16px;top:98px;
    list-style:none;text-align:right;
    color:var(--white);font-size:12px;line-height:22px;
  }
  .contact-list li{display:flex;justify-content:flex-end;align-items:center;gap:7px;white-space:nowrap}
  .contact-list svg{width:13px;height:13px;flex:none}
</style>
</head>
<body>

<section class="card card-front" aria-label="Business card, logo side">
  <div class="wordmark">Quorvastem</div>
  <div class="website">www.quorvastem.com</div>
</section>

<section class="card card-back" aria-label="Business card, contact side">
  <svg class="artwork" viewBox="0 0 600 343" width="600" height="343" aria-hidden="true">
    <!-- grey contact panel -->
    <path d="M600,40 C470,48 380,96 340,180 C300,262 240,296 140,304 C80,308 40,309 0,309 L0,343 L600,343 Z" fill="var(--panel-grey)"/>
    <!-- soft shading along panel edge -->
    <path d="M600,40 C470,48 380,96 340,180 C400,112 490,80 600,72 Z" fill="var(--panel-grey-dark)" opacity=".5"/>
    <!-- blue ribbon following the panel edge -->
    <path d="M600,24 C465,32 372,82 330,168 C290,250 232,286 140,294 C80,298 40,299 0,299 L0,306 C40,306 80,305 140,301 C236,293 296,258 336,172 C378,88 468,40 600,32 Z" fill="var(--brand-blue)"/>
  </svg>

  <div class="wordmark">Quorvastem</div>

  <div class="holder">
    <div class="holder-name">John Doe</div>
    <div class="holder-role">Manager</div>
  </div>

  <ul class="contact-list">
    <li>111-222-333
      <svg viewBox="0 0 16 16"><path d="M4 1.5l2.2 3-1.4 1.6c.8 1.8 2.2 3.3 4.1 4.1l1.6-1.4 3 2.2-1 2.6C7 13.4 2.6 9 1.4 2.5z" fill="var(--brand-blue-light)"/></svg>
    </li>
    <li>info@quorvastem.com
      <svg viewBox="0 0 16 16"><rect x="1.5" y="3.5" width="13" height="9" rx="1" fill="none" stroke="var(--brand-blue-light)" stroke-width="1.6"/><path d="M2 4.5l6 4.5 6-4.5" fill="none" stroke="var(--brand-blue-light)" stroke-width="1.6"/></svg>
    </li>
    <li>www.quorvastem.com
      <svg viewBox="0 0 16 16"><circle cx="8" cy="8" r="6.3" fill="none" stroke="var(--brand-blue-light)" stroke-width="1.5"/><path d="M1.8 8h12.4M8 1.7c-3 3.5-3 9.1 0 12.6M8 1.7c3 3.5 3 9.1 0 12.6" fill="none" stroke="var(--brand-blue-light)" stroke-width="1.2"/></svg>
    </li>
    <li>12345 your street here, country
      <svg viewBox="0 0 16 16"><path d="M8 15s5-5.2 5-8.8A5 5 0 0 0 3 6.2C3 9.8 8 15 8 15z" fill="var(--brand-blue-light)"/><circle cx="8" cy="6.3" r="1.8" fill="var(--panel-grey)"/></svg>
    </li>
  </ul>
</section>

</body>
</html>
```